Personal training studio poster / postcard

We need a poster / postcard design to advertise our recently established personal training studio - details and logo in the attached file. Logo file also provided.

We are flexible on format. Prefer the use of pictures in the design.

Training

```html
<!DOCTYPE html>
<html lang="en">
<head>
<meta charset="utf-8">
<title>Ridgeway Strength Studio – Poster</title>
<link rel="stylesheet" href="https://fonts.googleapis.com/css2?family=Oswald:wght@600&family=Pathway+Gothic+One&display=swap">
<style>
  :root {
    --bg: #050505;
    --ink: #ffffff;
    --muted: #9a9a9a;
    --silver-light: #f2f2f2;
    --silver-mid: #b9b9b9;
    --silver-dark: #6d6d6d;
    --band-light: #8e8e8e;
    --band-dark: #4a4a4a;
    --chip: #2a2a2a;
    --numeral: #3a3a3a;
    --icon-grey: #555555;
    --icon-blue: #2f6fb8;
    --icon-green: #5aa02c;
    --icon-red: #c4161c;
    --brand: #d8d8d8;
  }
  * { box-sizing: border-box; margin: 0; padding: 0; }
  html, body { width: 847px; height: 1200px; overflow: hidden; background: var(--bg); }
  .poster {
    position: relative; width: 847px; height: 1200px; overflow: hidden;
    background: var(--bg);
    font-family: "Pathway Gothic One", "Arial Narrow", sans-serif;
    color: var(--ink);
  }
  .swooshes { position: absolute; inset: 0; }

  .brand {
    position: absolute; top: 88px; left: 0; width: 100%;
    text-align: center; font-size: 62px; line-height: 1;
    letter-spacing: 3px; text-transform: uppercase; color: var(--brand);
  }
  .tagline {
    position: absolute; top: 230px; left: 0; width: 100%;
    text-align: center; font-size: 25px; color: #c8c8c8; letter-spacing: .5px;
  }

  .services-title { position: absolute; left: 81px; top: 390px; font-size: 44px; }
  .services-sub { position: absolute; left: 81px; top: 452px; font-size: 26px; color: var(--muted); }

  .service-list { position: absolute; left: 82px; top: 538px; list-style: none; }
  .service {
    display: flex; align-items: center; height: 44px; margin-bottom: 19.5px;
  }
  .service-icon {
    width: 40px; height: 40px; border-radius: 50%; flex: none;
    border: 2px solid #cfcfcf; box-shadow: 0 2px 4px rgba(0,0,0,.6);
  }
  .service-label {
    margin-left: 14px; padding: 0 7px; height: 38px; line-height: 38px;
    font-size: 30px; letter-spacing: .3px;
    background: linear-gradient(#3a3a3a, #1a1a1a);
    border-radius: 2px; text-shadow: 0 1px 2px #000;
  }
  .icon-grey { background: radial-gradient(circle at 35% 30%, #8a8a8a, var(--icon-grey) 60%, #222); }
  .icon-blue { background: radial-gradient(circle at 35% 30%, #6ea6e8, var(--icon-blue) 60%, #123a6a); }
  .icon-green { background: radial-gradient(circle at 35% 30%, #9fd46a, var(--icon-green) 60%, #24520f); }
  .icon-red { background: radial-gradient(circle at 35% 30%, #f06868, var(--icon-red) 60%, #5e0709); }

  .medallion {
    position: absolute; border-radius: 50%;
    background: linear-gradient(145deg, #fafafa, var(--silver-dark) 45%, #2a2a2a 70%, var(--silver-mid));
    box-shadow: 0 6px 14px rgba(0,0,0,.8);
    display: flex; align-items: center; justify-content: center;
  }
  .medallion-face {
    border-radius: 50%; text-align: center; color: #222;
    background: radial-gradient(circle at 45% 35%, #ffffff, var(--silver-light) 50%, #bdbdbd);
    display: flex; flex-direction: column; align-items: center; justify-content: center;
  }
  .special { left: 399px; top: 308px; width: 196px; height: 196px; }
  .special .medallion-face { width: 172px; height: 172px; }
  .special-title { font-size: 31px; line-height: 1.05; }
  .special-text { font-size: 24px; line-height: 1.1; color: #333; }
  .special-text strong { font-weight: normal; font-size: 28px; color: #111; }
  .shoe { width: 70px; height: 30px; margin-top: 6px; border-radius: 14px 18px 6px 6px;
    background: linear-gradient(#e9e9e9, #b8b8b8); }

  .booking { left: 524px; top: 465px; width: 246px; height: 246px; }
  .booking .medallion-face { width: 214px; height: 214px; }
  .booking-title { font-size: 34px; line-height: 1.1; margin-bottom: 6px; }
  .booking-line { font-family: "Arial Narrow", Arial, sans-serif; font-size: 11px; line-height: 1.65; color: #111; }

  .schedule { position: absolute; right: 0; width: 400px; }
  .schedule-band {
    position: absolute; inset: 0 0 0 30px;
    background: linear-gradient(180deg, var(--band-light), var(--band-dark));
    border-radius: 6px 0 0 6px;
    clip-path: polygon(0 0, 100% 0, 100% 100%, 6% 100%);
  }
  .schedule-num {
    position: absolute; left: 0; top: 50%; transform: translateY(-50%);
    font-family: "Oswald", Impact, sans-serif; font-weight: 600;
    font-size: 150px; line-height: 1; color: var(--numeral);
    text-shadow: 1px 1px 0 #777;
  }
  .schedule-text {
    position: absolute; left: 100px; top: 50%; transform: translateY(-50%);
    font-size: 35px; line-height: 1.12; text-shadow: 0 1px 3px #222;
  }
  .schedule-icon {
    position: absolute; right: 40px; top: 50%; transform: translateY(-50%);
    width: 72px; height: 72px; border-radius: 42% 50% 44% 50%;
    background: radial-gradient(circle at 40% 30%, #8a8a8a, #2a2a2a 60%, #111);
    border: 2px solid #cfcfcf;
  }
  .slot-1 { top: 796px; height: 100px; }
  .slot-2 { top: 907px; height: 115px; }
  .slot-3 { top: 1033px; height: 115px; }
</style>
</head>
<body>
<main class="poster">
  <svg class="swooshes" width="847" height="1200" viewBox="0 0 847 1200" aria-hidden="true">
    <defs>
      <linearGradient id="swoosh-fade" x1="0" x2="1">
        <stop offset="0" stop-color="#6a6a6a"/>
        <stop offset="1" stop-color="#1a1a1a"/>
      </linearGradient>
    </defs>
    <path d="M-20 90 C200 40 420 30 847 60" stroke="url(#swoosh-fade)" stroke-width="3" fill="none"/>
    <path d="M-20 150 C120 100 240 80 330 70" stroke="#3a3a3a" stroke-width="14" fill="none"/>
    <path d="M-20 250 C80 180 180 130 300 110" stroke="#2a2a2a" stroke-width="22" fill="none"/>
    <path d="M-20 520 C60 380 140 300 300 250" stroke="#1d1d1d" stroke-width="30" fill="none"/>
    <path d="M560 40 C700 20 800 30 847 40" stroke="#4a4a4a" stroke-width="10" fill="none"/>
    <path d="M600 140 C720 110 800 110 847 120" stroke="#2a2a2a" stroke-width="16" fill="none"/>
    <path d="M0 1130 C200 1000 320 930 450 900" stroke="#1b1b1b" stroke-width="40" fill="none"/>
    <path d="M0 1200 C150 1100 300 1040 450 1010" stroke="#141414" stroke-width="40" fill="none"/>
  </svg>

  <h1 class="brand">Ridgeway Strength Studio</h1>
  <p class="tagline">Boutique personal and small group training studio</p>

  <h2 class="services-title">Personal training</h2>
  <p class="services-sub">Group fitness classes</p>

  <ul class="service-list">
    <li class="service"><span class="service-icon icon-grey" role="img" aria-label="Yoga pictogram"></span><span class="service-label">Yoga</span></li>
    <li class="service"><span class="service-icon icon-grey" role="img" aria-label="Martial arts pictogram"></span><span class="service-label">MMA conditioning</span></li>
    <li class="service"><span class="service-icon icon-grey" role="img" aria-label="Weightlifting pictogram"></span><span class="service-label">Strength circuit</span></li>
    <li class="service"><span class="service-icon icon-blue" role="img" aria-label="Body assessment pictogram"></span><span class="service-label">Body signature assessment</span></li>
    <li class="service"><span class="service-icon icon-green" role="img" aria-label="Nutrition pictogram"></span><span class="service-label">Nutrition advice</span></li>
    <li class="service"><span class="service-icon icon-red" role="img" aria-label="Treatment table pictogram"></span><span class="service-label">Osteopathy</span></li>
  </ul>

  <section class="medallion special">
    <div class="medallion-face">
      <p class="special-title">August special</p>
      <p class="special-text">all group fitness<br>classes <strong>$10</strong></p>
      <div class="shoe" role="img" aria-label="Pair of running shoes"></div>
    </div>
  </section>

  <section class="medallion booking">
    <div class="medallion-face">
      <p class="booking-title">Book online</p>
      <p class="booking-line"><strong>www.ridgewaystrengthstudio.com.au</strong></p>
      <p class="booking-line">or phone</p>
      <p class="booking-line">0412 555 208</p>
      <p class="booking-line">1/14 Harbour Lane Ridgeway</p>
    </div>
  </section>

  <section class="schedule slot-1">
    <div class="schedule-band"></div>
    <span class="schedule-num">1</span>
    <p class="schedule-text">Tuesdays 6:15am</p>
    <span class="schedule-icon" role="img" aria-label="Weightlifting pictogram"></span>
  </section>
  <section class="schedule slot-2">
    <div class="schedule-band"></div>
    <span class="schedule-num">2</span>
    <p class="schedule-text">Tuesdays &amp;<br>Thursdays 6:15pm</p>
    <span class="schedule-icon" role="img" aria-label="Yoga pictogram"></span>
  </section>
  <section class="schedule slot-3">
    <div class="schedule-band"></div>
    <span class="schedule-num">3</span>
    <p class="schedule-text">Saturdays 9am</p>
    <span class="schedule-icon" role="img" aria-label="Martial arts pictogram"></span>
  </section>
</main>
</body>
</html>
```